Business Card Design

Provide project management services to the construction and other industries
Construction services - Civil and Concrete works
Shop Detailing
Structural Modelling
Client side coordination of project teams and consultants
Feasibility Studies for construction projects

Industry/Entity Type

Business

Contact Information for Business Card

Plan Sure
Derek Calloway B.Sc (Eng), M.P.Mgt.
Director

m: 0412 738 564
e: dcalloway@plansure.com.au

p: 08 6358 2714
a: 17 Banksia Court, Wattleby, WA 6099

```html
<!DOCTYPE html>
<html lang="en">
<head>
<meta charset="utf-8">
<title>Plan Sure – Business Card</title>
<link href="https://fonts.googleapis.com/css2?family=Oswald:wght@400;600;700&family=Open+Sans:wght@400;600&family=Roboto+Condensed:wght@400;700&display=swap" rel="stylesheet">
<style>
  :root {
    --bg: #e9e9e6;
    --white: #ffffff;
    --ink: #111111;
    --grey-band: #c9c9c9;
    --green: #1f9a1f;
    --green-deep: #0d6e0d;
    --green-bright: #22b81c;
    --pill: rgba(0, 45, 0, 0.55);
  }
  * { box-sizing: border-box; margin: 0; padding: 0; }
  html, body { width: 1200px; height: 1024px; overflow: hidden; }
  body {
    background: var(--bg);
    display: flex;
    flex-direction: column;
    align-items: center;
    justify-content: center;
    gap: 64px;
    font-family: "Open Sans", sans-serif;
  }
  .card {
    position: relative;
    width: 700px;
    height: 400px;
    border-radius: 30px;
    overflow: hidden;
    box-shadow: 0 6px 18px rgba(0,0,0,0.18);
  }

  /* Front */
  .card-front { background: var(--white); }
  .front-wave { position: absolute; inset: 0; width: 100%; height: 100%; }
  .brand {
    font-family: "Oswald", sans-serif;
    font-weight: 700;
    text-transform: uppercase;
    letter-spacing: 1px;
    line-height: 1;
  }
  .front-brand {
    position: absolute;
    left: 46px; top: 96px;
    font-size: 56px;
    color: var(--ink);
  }
  .front-rule {
    position: absolute;
    left: 46px; top: 190px;
    width: 250px; height: 1.5px;
    background: var(--ink);
  }
  .contact-list {
    position: absolute;
    left: 50px; top: 212px;
    list-style: none;
    font-size: 15px;
    color: var(--ink);
  }
  .contact-list li {
    display: flex; align-items: center; gap: 14px;
    height: 28px;
  }
  .contact-list svg { width: 14px; height: 14px; fill: var(--green); flex: none; }
  .person {
    position: absolute;
    left: 420px; top: 34px;
    width: 250px;
  }
  .person-rule { height: 1.5px; background: var(--ink); margin-bottom: 8px; }
  .person-name {
    font-family: "Oswald", sans-serif;
    font-weight: 600;
    font-size: 26px;
    color: var(--ink);
    text-transform: uppercase;
    line-height: 1.1;
  }
  .person-quals {
    font-family: "Oswald", sans-serif;
    font-weight: 400;
    font-size: 17px;
    color: var(--green);
    text-transform: uppercase;
    letter-spacing: 0.5px;
  }
  .person-role {
    font-family: "Oswald", sans-serif;
    font-size: 14px;
    color: var(--ink);
  }

  /* Back */
  .card-back {
    background: radial-gradient(ellipse at 55% 20%, var(--green-bright) 0%, var(--green) 45%, var(--green-deep) 100%);
  }
  .service-list {
    position: absolute;
    left: 34px; top: 44px;
    list-style: none;
    font-family: "Roboto Condensed", sans-serif;
    font-size: 17px;
    color: var(--white);
  }
  .service-list li {
    display: flex; align-items: center; gap: 8px;
    width: fit-content;
    background: var(--pill);
    border-radius: 14px;
    padding: 3px 14px 3px 10px;
    margin-bottom: 10px;
  }
  .service-list svg { width: 14px; height: 14px; fill: none; stroke: var(--white); stroke-width: 2.6; flex: none; }
  .back-brand {
    position: absolute;
    right: 46px; bottom: 64px;
    font-size: 58px;
    color: var(--white);
  }
</style>
</head>
<body>

<section class="card card-front" aria-label="Business card front">
  <svg class="front-wave" viewBox="0 0 700 400" preserveAspectRatio="none" aria-hidden="true">
    <path d="M0 366 C 220 366, 360 350, 440 290 C 510 220, 560 110, 700 96 L700 400 L0 400 Z" fill="var(--grey-band)"/>
    <path d="M0 378 C 230 378, 380 362, 460 300 C 530 236, 580 130, 700 116 L700 400 L0 400 Z" fill="var(--green)"/>
  </svg>

  <div class="brand front-brand">Plan Sure</div>
  <div class="front-rule"></div>

  <ul class="contact-list">
    <li>
      <svg viewBox="0 0 16 16" aria-hidden="true"><path d="M4 1h8a1 1 0 0 1 1 1v12a1 1 0 0 1-1 1H4a1 1 0 0 1-1-1V2a1 1 0 0 1 1-1zm1 2v9h6V3z"/></svg>
      0412 738 564
    </li>
    <li>
      <svg viewBox="0 0 16 16" aria-hidden="true"><path d="M1 3h14v10H1zm1.5 1.2V5l5.5 4 5.5-4v-.8z"/></svg>
      dcalloway@plansure.com.au
    </li>
    <li>
      <svg viewBox="0 0 16 16" aria-hidden="true"><path d="M3.6 1.5l2.3 2.8-1.3 1.6a9 9 0 0 0 5.5 5.5l1.6-1.3 2.8 2.3-1.7 2.1C7 14 2 9 1.5 3.2z"/></svg>
      08 6358 2714
    </li>
    <li>
      <svg viewBox="0 0 16 16" aria-hidden="true"><path d="M8 1a5 5 0 0 1 5 5c0 3.6-5 9-5 9S3 9.6 3 6a5 5 0 0 1 5-5zm0 3a2 2 0 1 0 0 4 2 2 0 0 0 0-4z"/></svg>
      17 Banksia Court, Wattleby, WA 6099
    </li>
  </ul>

  <div class="person">
    <div class="person-rule"></div>
    <div class="person-name">Derek Calloway</div>
    <div class="person-quals">B.Sc (Eng), M.P.Mgt.</div>
    <div class="person-role">Director</div>
  </div>
</section>

<section class="card card-back" aria-label="Business card back">
  <ul class="service-list">
    <li><svg viewBox="0 0 16 16" aria-hidden="true"><path d="M2 8.5l4 4 8-9"/></svg>Construction services - Civil and Concrete works</li>
    <li><svg viewBox="0 0 16 16" aria-hidden="true"><path d="M2 8.5l4 4 8-9"/></svg>Shop Detailing</li>
    <li><svg viewBox="0 0 16 16" aria-hidden="true"><path d="M2 8.5l4 4 8-9"/></svg>Structural Modelling</li>
    <li><svg viewBox="0 0 16 16" aria-hidden="true"><path d="M2 8.5l4 4 8-9"/></svg>Client side coordination of project teams and consultants</li>
    <li><svg viewBox="0 0 16 16" aria-hidden="true"><path d="M2 8.5l4 4 8-9"/></svg>Feasibility Studies for construction projects</li>
  </ul>
  <div class="brand back-brand">Plan Sure</div>
</section>

</body>
</html>
```